1. Need design for shock abosrber box.
2. attach is the old box model.

3. Brand: TORVEK
4. i want word: SUPER SHOCKS (pls design unique font for this words)
to show strength and durability.

Box has 2 size:
1. 8cm x 8cm x 46cm
2. 22cm x 22cm x 46cm
(more or less)

Dear all,

1. HELDISON and attached file is old model box n design. We want new out of the box design.
2. TORVEK is the new brand. SUPER SHOCKS is the slogan.
3. We attached some existing brands for your reference. Expecting a design that can top all those existing brand box design.

Dear All,

We would like to see something out of the box. You got to top the existing brands, which files i attached already.
Preference more to Corvanto style.

thanks,
Gerald.

Reason: 1. to give all designers enough time to submit quality design, i will extend the deadline 14 days.

Dear All,

In simple words, pls follow Corvanto concept for reference. I am ok with it.
I attached many pictures of Corvanto and you also can search easily in web.
I really expect something not too far from Corvanto concept.

Reason: Dear All, Please understand, i would like to give all designers enough time to submit their best design.

Font styles to use
Serif
Script

Colors
0491cc
34a7d8
86cae7
cee9f5
ecf7fb
ffffff

Requirements
Nice to have
• 1. area for car pictures (just like in old model box), that i can modify your file later on, with different car picture, depend on target car brand.

Wordings:
1. TORVEK SUPER SHOCKS / TORVEK SUPER SHOCK ABSORBER.
2. SUPER STRONG
3. MAXIMUM DURABILITY & PERFORMANCE.

can i have a japanese SUMO silhouette carrying a shock absorber. (if possible) at one side corner.

```html
<!DOCTYPE html>
<html lang="en">
<head>
<meta charset="utf-8">
<title>TORVEK Super Shocks – Box Dieline</title>
<link href="https://fonts.googleapis.com/css2?family=Oswald:wght@500;700&family=Arimo:wght@400;700&display=swap" rel="stylesheet">
<style>
  :root {
    --stage-light: #f4f4f4;
    --stage-dark: #d9d9d9;
    --kraft: #b3835a;
    --kraft-fold: #c89c74;
    --track: rgba(128, 78, 52, 0.55);
    --band-red: #94282b;
    --ink: #231f20;
    --paper: #ffffff;
    --product: #f3f3f3;
  }
  * { margin: 0; padding: 0; box-sizing: border-box; }
  html, body { width: 1200px; height: 841px; overflow: hidden; }
  body {
    background: radial-gradient(ellipse at center, var(--stage-light) 35%, var(--stage-dark) 100%);
    font-family: "Arimo", Arial, sans-serif;
  }
  .dieline { position: relative; width: 1200px; height: 841px; }
  .dieline-art { position: absolute; inset: 0; }

  .brand-name {
    position: absolute;
    font-family: "Oswald", sans-serif;
    font-weight: 700;
    color: var(--ink);
    line-height: 1;
    white-space: nowrap;
  }
  .brand-name--top { left: 272px; top: 156px; font-size: 62px; letter-spacing: 20px; }
  .brand-name--bottom { left: 605px; top: 575px; font-size: 64px; letter-spacing: 20px; }
  .brand-tm {
    position: absolute;
    font-family: "Arimo", sans-serif;
    font-size: 13px;
    color: var(--ink);
  }
  .brand-tm--top { left: 597px; top: 132px; }
  .brand-tm--bottom { left: 928px; top: 556px; }

  .slogan {
    position: absolute;
    font-family: "Oswald", sans-serif;
    font-weight: 700;
    color: var(--paper);
    line-height: 1;
    letter-spacing: 1px;
    white-space: nowrap;
  }
  .slogan--top { left: 435px; top: 222px; font-size: 32px; }
  .slogan--bottom { left: 765px; top: 644px; font-size: 33px; }

  .flap-logo {
    position: absolute;
    left: 12px; top: 318px;
    width: 120px;
    transform: rotate(-90deg);
    transform-origin: center;
    font-family: "Oswald", sans-serif;
    font-weight: 700;
    font-size: 30px;
    color: var(--ink);
    letter-spacing: 2px;
    text-align: center;
  }
  .flap-slogan {
    position: absolute;
    left: 48px; top: 320px;
    width: 110px;
    transform: rotate(90deg);
    font-family: "Oswald", sans-serif;
    font-weight: 700;
    font-size: 11px;
    color: var(--paper);
    text-align: center;
  }

  .upside-down { position: absolute; transform: rotate(180deg); }

  .thanks-copy {
    left: 210px; top: 416px; width: 250px;
    font-size: 6.6px;
    line-height: 8.6px;
    color: var(--ink);
    text-align: center;
    text-transform: uppercase;
  }
  .thanks-copy .thanks-title { margin-bottom: 9px; }

  .feature-list {
    left: 716px; top: 408px; width: 280px;
    list-style: none;
    font-size: 8.6px;
    color: var(--ink);
    text-transform: uppercase;
  }
  .feature-list li {
    display: flex; align-items: center; gap: 8px;
    height: 28.6px;
  }
  .feature-icon {
    width: 18px; height: 18px; border-radius: 50%;
    background: var(--ink);
    flex: 0 0 18px;
    display: flex; align-items: center; justify-content: center;
  }
  .feature-icon svg { width: 12px; height: 12px; }

  .barcode-panel {
    position: absolute;
    left: 1026px; top: 268px; width: 93px; height: 125px;
    background: var(--paper);
  }
</style>
</head>
<body>
<main class="dieline">
  <svg class="dieline-art" width="1200" height="841" viewBox="0 0 1200 841" xmlns="http://www.w3.org/2000/svg">
    <g class="board" fill="var(--kraft)">
      <rect x="197" y="120" width="806" height="598" />
      <polygon points="197,124 129,150 129,257 197,257" />
      <polygon points="1003,124 1071,150 1071,257 1003,257" />
      <polygon points="197,262 28,262 10,280 10,383 28,401 197,401" />
      <polygon points="1003,262 1172,262 1190,280 1190,383 1172,401 1003,401" />
      <polygon points="197,404 140,410 129,420 129,512 197,542" />
      <polygon points="1003,404 1060,410 1071,420 1071,512 1003,542" />
    </g>
    <polygon points="197,694 197,718 223,718" fill="var(--stage-light)" />
    <polygon points="1003,694 1003,718 977,718" fill="var(--stage-light)" />

    <polygon class="tread-area" role="img" aria-label="Tyre tread track decoration"
             points="891,120 1003,120 1003,330 737,718 506,718" fill="var(--track)" />

    <g class="fold-lines" stroke="var(--kraft-fold)" stroke-width="1">
      <line x1="197" y1="257" x2="1003" y2="257" />
      <line x1="197" y1="401" x2="1003" y2="401" />
      <line x1="197" y1="542" x2="1003" y2="542" />
      <line x1="197" y1="124" x2="197" y2="694" />
      <line x1="1003" y1="124" x2="1003" y2="694" />
    </g>

    <g class="brand-bands" fill="var(--band-red)">
      <rect x="197" y="160" width="806" height="3" />
      <rect x="197" y="166" width="806" height="45" />
      <rect x="197" y="214" width="806" height="3" />
      <rect x="197" y="584" width="806" height="3" />
      <rect x="197" y="590" width="806" height="45" />
      <rect x="197" y="638" width="806" height="3" />
    </g>

    <rect class="mascot-area" role="img" aria-label="Sumo wrestler silhouette lifting a shock absorber"
          x="904" y="156" width="90" height="101" fill="var(--ink)" opacity="0.85" />

    <g class="recycle-mark" transform="translate(981 281)" fill="none" stroke="var(--ink)" stroke-width="3">
      <circle r="13" />
      <path d="M-6 -2 A7 7 0 0 1 6 -3 M6 2 A7 7 0 0 1 -6 3" stroke-width="2.5" />
    </g>

    <rect class="product-area" role="img" aria-label="Line drawing of a shock absorber"
          x="561" y="114" width="70" height="603" rx="28"
          transform="rotate(30 596 415)" fill="var(--product)" stroke="#cfcfcf" stroke-width="1" />
  </svg>

  <div class="brand-name brand-name--top">TORVEK</div>
  <div class="brand-tm brand-tm--top">TM</div>
  <div class="slogan slogan--top">SUPER SHOCKS</div>

  <div class="brand-name brand-name--bottom">TORVEK</div>
  <div class="brand-tm brand-tm--bottom">TM</div>
  <div class="slogan slogan--bottom">SUPER SHOCKS</div>

  <div class="flap-logo">TORVEK</div>
  <div class="flap-slogan">SUPER SHOCKS</div>

  <div class="barcode-panel"></div>

  <div class="upside-down thanks-copy">
    <p class="thanks-title">Thank you for choosing TORVEK!</p>
    <p>This product has been carefully manufactured using the latest technology and expertise garnered from years of successful competition racing. The extreme demands of competition have set the benchmark for TORVEK suspension systems. It is this fundamental principle that we strive to achieve when manufacturing our precision, state of the art suspension systems for both off-road and road products</p>
  </div>

  <ul class="upside-down feature-list">
    <li><span class="feature-icon"><svg viewBox="0 0 12 12"><path d="M1 7h10M6 7l-3-4h6z" stroke="#b3835a" fill="none" stroke-width="1.4"/></svg></span>Stability</li>
    <li><span class="feature-icon"><svg viewBox="0 0 12 12"><path d="M1 10l4-4 2 2 4-5" stroke="#b3835a" fill="none" stroke-width="1.4"/></svg></span>High performance</li>
    <li><span class="feature-icon"><svg viewBox="0 0 12 12"><circle cx="6" cy="6" r="1.6" fill="#b3835a"/><ellipse cx="6" cy="6" rx="5" ry="2" stroke="#b3835a" fill="none"/></svg></span>Superior technology</li>
    <li><span class="feature-icon"><svg viewBox="0 0 12 12"><path d="M2 8l3-3M7 4l3-3M4 10l6-6" stroke="#b3835a" fill="none" stroke-width="1.4"/></svg></span>Robust design and durability</li>
    <li><span class="feature-icon"><svg viewBox="0 0 12 12"><path d="M2 2h3v3H2zM7 2h3v3H7zM2 7h3v3H2zM7 7h3v3H7z" fill="#b3835a"/></svg></span>Technology derived from competition racing</li>
  </ul>
</main>
</body>
</html>
```